Business Card Design Project

I want a cleaner business card and envelope then what we have now, its too crowded.
Updates

I update with logo, this can be changed anyway you feel it looks best. I also have put gaurantee on there and extended time, this is my first time doing this. Also gave an example of current card

Target Market(s)

a wide array of customers from lattice 700 to small companies and cleints

Industry/Entity Type

Business

Requirements
Must have
• Need to have address, telephone number email
Nice to have
• a sharp professional card that stands out but is still very clean.
Should not have
• Not crazy looking

```html
<!DOCTYPE html>
<html lang="en">
<head>
<meta charset="utf-8">
<title>Harwell Insurance Group – Business Card</title>
<link rel="stylesheet" href="https://fonts.googleapis.com/css2?family=Michroma&display=swap">
<style>
  :root {
    --page: #ffffff;
    --card: #262626;      /* K 93% */
    --black: #000000;     /* K 100% */
    --green: #7ac143;     /* Pantone 376 */
    --white: #ffffff;
    --ink: #222222;
    --font: "Michroma", sans-serif;
  }
  * { box-sizing: border-box; margin: 0; padding: 0; }
  html, body { width: 927px; height: 1200px; overflow: hidden; background: var(--page); }
  body { position: relative; font-family: var(--font); color: var(--white); }

  .card-set { position: absolute; left: 50px; top: 430px; width: 827px; height: 229px; }
  .card {
    position: absolute; top: 0; width: 400px; height: 229px;
    background: var(--card); border-radius: 12px; overflow: hidden;
  }
  .card--front { left: 0; }
  .card--back { left: 427px; }
  .card__sweep { position: absolute; inset: 0; width: 100%; height: 100%; }

  .brand { position: absolute; top: 14px; left: 0; width: 100%; text-align: center; }
  .brand__mark { display: block; width: 34px; height: 34px; margin: 0 auto 8px; background: #8a8a8a; }
  .brand__name { font-size: 19px; letter-spacing: 2px; line-height: 1; }
  .brand__tag { font-size: 7.5px; letter-spacing: 1.6px; margin-top: 4px; }

  .rule { position: absolute; top: 117px; left: 0; width: 372px; height: 2px; background: var(--green); }

  .person { position: absolute; top: 132px; left: 0; width: 100%; text-align: center; }
  .person__name { font-size: 11px; letter-spacing: 1px; }
  .person__title { font-size: 7.5px; color: var(--green); margin-top: 5px; letter-spacing: .8px; }

  .contact { position: absolute; bottom: 14px; font-size: 6.2px; line-height: 1.5; letter-spacing: .5px; text-transform: uppercase; }
  .contact--left { left: 12px; }
  .contact--right { right: 14px; text-align: right; }

  .services { position: absolute; top: 128px; font-size: 6px; line-height: 1.5; letter-spacing: .5px; text-transform: uppercase; }
  .services--left { left: 12px; }
  .services--right { left: 206px; }
  .services h3 { font-weight: 400; font-size: 7.5px; color: var(--green); letter-spacing: .8px; }
  .services ul { list-style: none; margin-bottom: 6px; }
  .services li::before { content: "· "; }

  .swatches { position: absolute; top: 730px; left: 50px; width: 827px; display: flex; justify-content: space-between; padding-right: 40px; }
  .swatch { display: flex; align-items: center; gap: 16px; color: var(--ink); font-family: Arial, sans-serif; font-size: 15px; }
  .swatch__chip { width: 73px; height: 18px; }
</style>
</head>
<body>
  <main class="card-set">
    <section class="card card--front" aria-label="Card front">
      <svg class="card__sweep" viewBox="0 0 400 229" aria-hidden="true">
        <path d="M245,229 C300,170 320,95 400,55 L400,229 Z" fill="var(--black)"/>
      </svg>
      <div class="brand">
        <span class="brand__mark"></span>
        <div class="brand__name">HARWELL</div>
        <div class="brand__tag">INSURANCE GROUP</div>
      </div>
      <div class="rule"></div>
      <div class="person">
        <div class="person__name">MARLA QUENT-HOLLIS</div>
        <div class="person__title">OPERATIONS MANAGER</div>
      </div>
      <address class="contact contact--left" style="font-style:normal">
        Phone: 555-010-4400 ext. 232<br>
        Direct: 555-010-4418<br>
        Fax: 555-010-4403<br>
        mquent-hollis@harwellagency.com
      </address>
      <address class="contact contact--right" style="font-style:normal">
        1820 Alder Crest Ave<br>
        Fenwick Heights, MI 40012<br>
        www.harwellagency.com
      </address>
    </section>

    <section class="card card--back" aria-label="Card back">
      <svg class="card__sweep" viewBox="0 0 400 229" aria-hidden="true">
        <path d="M175,229 C215,160 200,75 230,0 L400,0 L400,229 Z" fill="var(--black)"/>
      </svg>
      <div class="brand">
        <span class="brand__mark"></span>
        <div class="brand__name">HARWELL</div>
        <div class="brand__tag">INSURANCE GROUP</div>
      </div>
      <div class="rule"></div>
      <div class="services services--left">
        <h3>COMMERCIAL INSURANCE</h3>
        <ul>
          <li>Traditional Insurance Coverage</li>
          <li>Executive Protection Coverage</li>
          <li>Specialty Coverage Insurance</li>
        </ul>
        <h3>PERSONAL INSURANCE</h3>
        <ul>
          <li>Auto/Recreational/Boat</li>
          <li>Home/Renters/Condo</li>
          <li>Umbrella Liability</li>
        </ul>
      </div>
      <div class="services services--right">
        <h3>EMPLOYEE BENEFITS</h3>
        <ul>
          <li>Medical/Dental/Optical Plans</li>
          <li>Prescription Coverage</li>
          <li>Life &amp; Accidental Death</li>
          <li>&amp; Dismemberment Insurance</li>
          <li>Disability Insurance</li>
          <li>Voluntary Benefits</li>
        </ul>
      </div>
    </section>
  </main>

  <footer class="swatches">
    <div class="swatch"><span class="swatch__chip" style="background:var(--green)"></span>Pantone 376</div>
    <div class="swatch"><span class="swatch__chip" style="background:var(--card)"></span>K 93%</div>
    <div class="swatch"><span class="swatch__chip" style="background:var(--black)"></span>K 100%</div>
  </footer>
</body>
</html>
```